Copper Fern Photography

Internet sales of landscape photography
Some background on the name.... I'm originally from Kentucky hence the "Copper" and I now live in California wine country, hence the "Fern." The blue coloring in the name is from the Harlow Falcons and the name "photography" is done in a bourbon lettering font. Hope this helps.
Updates
Please include email as dennis@copperfernphotography.com
Please make website www.copperfernphotography.com and ad QR code if possible.
Industry/Entity Type
Landscape
Contact Information for Business Card
Dennis Marlowe
www.copperfernphoto.com
707-555-0192
Requirements
Must have
- My design logo, all contact info :)
I like the thought of a QR Code along with the written link also.

```html
<!DOCTYPE html>
<html lang="en">
<head>
<meta charset="utf-8">
<title>Copper Fern Photography — Business Card</title>
<link href="https://fonts.googleapis.com/css2?family=Roboto+Condensed:wght@400&display=swap" rel="stylesheet">
<style>
  :root {
    --bg-deep: #7d9fb8;
    --bg-mid: #a9c2d2;
    --bg-light: #d9e7ee;
    --bg-glow: #eef5f8;
    --brand-blue: #1f5ca6;
    --ink: #161616;
    --code-fill: #ffffff;
    --code-edge: #161616;
  }
  html, body {
    margin: 0;
    padding: 0;
    width: 1200px;
    height: 703px;
    overflow: hidden;
  }
  .card {
    position: relative;
    width: 1200px;
    height: 703px;
    overflow: hidden;
    font-family: "Roboto Condensed", "Arial Narrow", sans-serif;
  }
  .card__backdrop {
    position: absolute;
    inset: 0;
    background:
      radial-gradient(circle at 82% 22%, var(--bg-glow) 0, rgba(238,245,248,0) 28%),
      radial-gradient(circle at 30% 80%, rgba(238,245,248,0.7) 0, rgba(238,245,248,0) 32%),
      linear-gradient(160deg, var(--bg-deep) 0%, var(--bg-mid) 40%, var(--bg-light) 75%, var(--bg-mid) 100%);
  }
  .brand {
    position: absolute;
    left: 70px;
    top: 92px;
    color: var(--brand-blue);
    font-weight: 400;
    line-height: 1;
  }
  .brand__name {
    display: block;
    font-size: 150px;
    letter-spacing: 1px;
  }
  .brand__tagline {
    display: block;
    margin-top: 14px;
    margin-left: 110px;
    font-size: 58px;
    letter-spacing: 14px;
  }
  .qr-code {
    position: absolute;
    left: 70px;
    top: 450px;
    width: 190px;
    height: 190px;
    background: var(--code-fill);
    border: 6px solid var(--code-edge);
    box-sizing: border-box;
  }
  .contact {
    position: absolute;
    right: 69px;
    top: 400px;
    text-align: right;
    color: var(--ink);
    font-weight: 400;
  }
  .contact__name {
    margin: 0 0 4px;
    font-size: 56px;
    line-height: 66px;
  }
  .contact__line {
    margin: 0;
    font-size: 40px;
    line-height: 58px;
  }
</style>
</head>
<body>
  <main class="card">
    <div class="card__backdrop" role="img" aria-label="Soft blue bokeh light background"></div>

    <div class="brand">
      <span class="brand__name">Copper Fern</span>
      <span class="brand__tagline">PHOTOGRAPHY</span>
    </div>

    <div class="qr-code" role="img" aria-label="QR code linking to www.copperfernphotography.com"></div>

    <div class="contact">
      <p class="contact__name">Dennis Marlowe</p>
      <p class="contact__line">dennis@copperfernphotography.com</p>
      <p class="contact__line">www.copperfernphotography.com</p>
      <p class="contact__line">Phone: 707-555-0192</p>
    </div>
  </main>
</body>
</html>
```